Honesty box for charity and people with disabilities

Please design an honesty box that stands out and makes people want to help. include the following
* we have been in business since 2007
* we employ people with disabilities
* we support Australian based charities
* all items are $2.60 each
*Thank you for choosing to support our box.

By supporting Moth’s Lantern you are insuring your valued money is going to make a real difference!!!

Real jobs for people with Disabilities

Real support for Australian Charities.

The Honesty Box that Honestly makes a difference!!!

* would like to change logo a bit. Open to ideas but would like to keep the bee.

* also would look at different wording. You can visit our website to get an idea of what we do. www.glowjarcharity.com.au

*for a refill or more information please visit www.glowjarcharity.com.au we have 2 types of boxes a yellow box and a bigger box it is the bigger box on the website that we need art work for not the yellow one

Also under supporting Australian charities need to put see website for charities we support.

Target Market(s)

18-60 years old

Industry/Entity Type

Business

Logo Text

Moth's Lantern

Font styles to use
Sans Serif

Colors
0255a3
ec1f27
fbed22
1b1b1b

Requirements
Must have
• wording of what we do must stand out that we employe people with disabilities.
• Make it priority
Nice to have
• A nice colourful box
Should not have
• Moth's Lantern lollie tray file this is an old box design please disregard the art work on the box
• The box should not look anything like the old box in the picture I only posted this for the box dimensions

```html
<!DOCTYPE html>
<html lang="en">
<head>
<meta charset="utf-8">
<title>Honesty Box Wrap Panels</title>
<link rel="stylesheet" href="https://fonts.googleapis.com/css2?family=Archivo+Black&family=Montserrat:wght@700;800&family=Open+Sans:wght@400&family=Oswald:wght@400;600&display=swap">
<style>
  :root {
    --yellow: #f5ec23;
    --red: #e2242a;
    --navy: #283482;
    --flag-light: #2f47b4;
    --flag-dark: #1b1f5e;
    --ink: #1b1b1b;
    --white: #ffffff;
    --rule: #c9c9c0;
  }
  html, body {
    margin: 0;
    padding: 0;
    width: 1200px;
    height: 1200px;
    overflow: hidden;
    background: var(--white);
  }
  .sheet { display: block; width: 1200px; height: 1200px; }
  .panel-outline { fill: var(--white); stroke: var(--rule); stroke-width: 1; }
  .field-yellow { fill: var(--yellow); }
  .band-red { fill: var(--red); }
  .field-white { fill: var(--white); }
  .logo-tile { fill: var(--navy); }
  .flag-area { fill: url(#flagTone); }
  .headline {
    font-family: "Oswald", sans-serif;
    font-weight: 600;
    fill: var(--white);
    text-anchor: middle;
  }
  .refill-info {
    font-family: "Oswald", sans-serif;
    font-weight: 400;
    font-size: 18px;
    fill: var(--red);
    text-anchor: middle;
  }
  .employee-note {
    font-family: "Open Sans", sans-serif;
    font-size: 22px;
    fill: var(--ink);
  }
  .logo-placeholder {
    font-family: "Open Sans", sans-serif;
    fill: var(--white);
    text-anchor: middle;
  }
  .price-label {
    font-family: "Montserrat", sans-serif;
    font-weight: 800;
    fill: var(--red);
    text-anchor: middle;
  }
  .price-figure { font-family: "Archivo Black", sans-serif; fill: var(--navy); }
  .price-each { font-family: "Archivo Black", sans-serif; fill: var(--red); text-anchor: middle; }
  .promise {
    font-family: "Montserrat", sans-serif;
    font-weight: 700;
    font-size: 14px;
    text-anchor: middle;
  }
  .promise--red { fill: var(--red); }
  .promise--navy { fill: var(--navy); }
  .tagline {
    font-family: "Montserrat", sans-serif;
    font-weight: 800;
    font-size: 14.5px;
    fill: var(--white);
    text-anchor: middle;
  }
</style>
</head>
<body>
<svg class="sheet" viewBox="0 0 1500 1500" xmlns="http://www.w3.org/2000/svg">
  <defs>
    <linearGradient id="flagTone" x1="0" y1="0" x2="1" y2="0.3">
      <stop offset="0" stop-color="#2f47b4"/>
      <stop offset="0.5" stop-color="#1b1f5e"/>
      <stop offset="1" stop-color="#2d42a8"/>
    </linearGradient>
  </defs>

  <g class="side-panel side-panel--a">
    <polygon class="panel-outline" points="133,139 1367,224 1367,422 133,422"/>
    <path class="field-yellow" d="M370,155 L990,198 C1030,240 1035,340 920,422 L506,422 C450,380 420,300 405,230 C385,200 395,175 370,155 Z"/>
    <path class="flag-area" role="img" aria-label="Waving Australian flag illustration"
          d="M133,139 L370,155 C395,175 385,200 405,230 C420,300 450,380 506,422 L133,422 Z"/>
    <path class="band-red" d="M410,241 L1018,241 C1024,262 1024,282 1020,302 L428,302 Z"/>
    <text class="headline" x="722" y="286" font-size="36" textLength="568" lengthAdjust="spacingAndGlyphs">PROUDLY SUPPORTING CHARITIES SINCE 2007</text>
    <text class="refill-info" x="695" y="335">for a refill or more information please visit</text>
    <text class="refill-info" x="695" y="360">www.glowjarcharity.com.au</text>
    <text class="refill-info" x="695" y="385">0400 111 222</text>
    <text class="employee-note" x="1083" y="298">space for a photo</text>
    <text class="employee-note" x="1083" y="327">and message from</text>
    <text class="employee-note" x="1083" y="356">your employees</text>
  </g>

  <g class="side-panel side-panel--b">
    <polygon class="panel-outline" points="133,550 1367,467 1367,750 133,750"/>
    <path class="field-yellow" d="M505,525 C470,560 470,680 580,750 L995,750 C1040,700 1070,640 1095,600 C1105,560 1100,530 1132,483 Z"/>
    <path class="flag-area" role="img" aria-label="Waving Australian flag illustration"
          d="M1132,483 L1367,467 L1367,750 L995,750 C1040,700 1070,640 1095,600 C1105,560 1100,530 1132,483 Z"/>
    <path class="band-red" d="M482,570 L1095,570 L1080,630 L477,630 C476,610 478,590 482,570 Z"/>
    <text class="headline" x="783" y="614" font-size="36" textLength="567" lengthAdjust="spacingAndGlyphs">PROUDLY SUPPORTING CHARITIES SINCE 2007</text>
    <text class="refill-info" x="805" y="663">for a refill or more information please visit</text>
    <text class="refill-info" x="805" y="688">www.glowjarcharity.com.au</text>
    <text class="refill-info" x="805" y="713">0400 111 222</text>
    <text class="employee-note" x="219" y="626">space for a photo</text>
    <text class="employee-note" x="219" y="655">and message from</text>
    <text class="employee-note" x="219" y="684">your employees</text>
  </g>

  <g class="front-panel">
    <path class="field-yellow" d="M265,822 L1243,822 L1235,830 L1235,1103 L1068,1103 L1064,1112 L929,1112 L925,1103 L265,1103 Z"/>
    <polygon class="band-red" points="257,822 265,822 265,832"/>
    <path class="flag-area" role="img" aria-label="Waving Australian flag illustration"
          d="M265,822 L462,822 C485,850 480,870 500,880 C540,970 560,1050 615,1103 L575,1112 L265,1103 Z"/>
    <rect class="band-red" x="511" y="875" width="509" height="47"/>
    <text class="headline" x="765" y="912" font-size="30" textLength="447" lengthAdjust="spacingAndGlyphs">PROUDLY SUPPORTING CHARITIES SINCE 2007</text>
    <rect class="field-white" x="640" y="974" width="220" height="60" rx="10"/>
    <rect class="logo-tile" x="1020" y="853" width="183" height="231"/>
    <text class="logo-placeholder" x="1111" y="928" font-size="40">your</text>
    <text class="logo-placeholder" x="1111" y="976" font-size="40">LOGO</text>
    <text class="logo-placeholder" x="1111" y="1024" font-size="40">here</text>
  </g>

  <g class="price-strip">
    <rect class="field-yellow" x="249" y="1163" width="1001" height="199"/>
    <path class="flag-area" role="img" aria-label="Waving Australian flag illustration"
          d="M249,1163 L425,1163 C440,1180 438,1200 445,1210 C460,1270 480,1330 515,1362 L249,1362 Z"/>
    <text class="price-label" x="594" y="1212" font-size="25" textLength="136" lengthAdjust="spacingAndGlyphs">ALL ITEMS</text>
    <text class="price-figure" x="522" y="1238" font-size="22">$</text>
    <text class="price-figure" x="540" y="1254" font-size="52" textLength="122" lengthAdjust="spacingAndGlyphs">2.60</text>
    <text class="price-each" x="593" y="1280" font-size="28" textLength="68" lengthAdjust="spacingAndGlyphs">each</text>
    <rect class="field-white" x="717" y="1194" width="328" height="97"/>
    <text class="promise promise--red" x="881" y="1220">Thank you for YOUR HONESTY</text>
    <text class="promise promise--navy" x="881" y="1247">Real jobs for people with Disabilities</text>
    <text class="promise promise--navy" x="881" y="1274">Real support for Australian Charities</text>
    <rect class="band-red" x="487" y="1316" width="620" height="25"/>
    <text class="tagline" x="796" y="1334">THE HONESTY BOX THAT HONESTLY GIVES BACK TO THE COMMUNITY</text>
    <rect class="logo-tile" x="1107" y="1173" width="133" height="169"/>
    <text class="logo-placeholder" x="1173" y="1228" font-size="28">your</text>
    <text class="logo-placeholder" x="1173" y="1263" font-size="28">LOGO</text>
    <text class="logo-placeholder" x="1173" y="1298" font-size="28">here</text>
  </g>
</svg>
</body>
</html>
```